Harborvale Ventures brochure for Investment partnership, young harold pembly

We need a brochure design to attract new investors for our investing partnership Called Harborvale Ventures. We are based in New Orleans, La. We primarily invest in stocks, bonds, and crypto but venture out into other categories as well. We would like to see designs with the black and gold like our logo. The final design should say new, fresh, sleek, tech, and honorable. BROUCHURE WILL BE 4 pages.or one folded sheet a paparer if that makes sense.
Updates

A chart showing Harborvale Ventures gains since 2019 28.6 percent and the TR 400 gAINS 7.1 PERCENT

Target Market(s)

Probable Investors

Industry/Entity Type

Financial Planning

Colors

Designer to choose only greyscale colors for use in the design.

Requirements
Must have
• Black and Gold accent. Stock market feel. Sleek, High tech, innovative, Intellgent design.
Nice to have
• Page colors possibly black.
Should not have
• Boring, Old school,

```html
<!DOCTYPE html>
<html lang="en">
<head>
<meta charset="utf-8">
<title>Harborvale Ventures – How it works</title>
<link rel="stylesheet" href="https://fonts.googleapis.com/css2?family=Source+Sans+3:wght@300;400;700&display=swap">
<style>
  :root {
    --page-black: #050505;
    --panel-brown: #2f2923;
    --panel-deep: #0b0a09;
    --gold: #f3dd47;
    --gold-glow: #e8c23a;
    --text-light: #ffffff;
    --text-soft: #e4e4e4;
    --bar-grey: #4a4a4a;
    --label-grey: #5a5a5a;
    --photo-blue-light: #9fc3da;
    --photo-blue-mid: #3f7296;
    --photo-blue-dark: #0f2a40;
  }
  * { margin: 0; padding: 0; box-sizing: border-box; }
  html, body { width: 1200px; height: 927px; overflow: hidden; background: var(--page-black); }
  .spread {
    position: relative;
    width: 1200px;
    height: 927px;
    overflow: hidden;
    background: var(--page-black);
    font-family: "Source Sans 3", "Helvetica Neue", Arial, sans-serif;
    color: var(--text-light);
  }
  .artwork { position: absolute; inset: 0; width: 1200px; height: 927px; }
  .intro {
    position: absolute;
    left: 70px;
    top: 424px;
    width: 250px;
    font-weight: 300;
    font-size: 21px;
    line-height: 33.2px;
    color: var(--text-light);
  }
  .steps-title {
    position: absolute;
    left: 636px;
    top: 536px;
    font-weight: 300;
    font-size: 36px;
    color: var(--gold);
    letter-spacing: 0.2px;
  }
  .steps {
    position: absolute;
    left: 636px;
    top: 598px;
    width: 300px;
    list-style: none;
    font-weight: 300;
    font-size: 12.4px;
    line-height: 16.4px;
    color: var(--text-soft);
  }
  .steps li { position: relative; padding-left: 37px; margin-bottom: 18px; }
  .steps li:nth-child(2) { margin-bottom: 17px; }
  .steps .step-num { position: absolute; left: 0; top: 0; }
  .gains-chart { position: absolute; left: 980px; top: 650px; width: 200px; height: 240px; }
  .bar-value { position: absolute; font-weight: 700; font-size: 16.5px; letter-spacing: 0.3px; }
  .bar-value.fund { left: 15px; top: 3px; color: var(--gold); }
  .bar-value.index { left: 131px; top: 100px; color: var(--label-grey); }
  .bar { position: absolute; bottom: 76px; width: 43px; }
  .bar.fund { left: 15px; height: 123px; background: var(--gold); }
  .bar.index { left: 131px; height: 31px; background: var(--bar-grey); }
  .bar-label {
    position: absolute;
    top: 177px;
    font-weight: 300;
    font-size: 13.8px;
    line-height: 18.3px;
    color: var(--text-soft);
  }
  .bar-label.fund { left: 10px; }
  .bar-label.index { left: 131px; }
</style>
</head>
<body>
<div class="spread">
  <svg class="artwork" viewBox="0 0 1200 927" xmlns="http://www.w3.org/2000/svg">
    <defs>
      <radialGradient id="heroTone" cx="0.6" cy="0.35" r="0.8">
        <stop offset="0" stop-color="var(--photo-blue-light)"/>
        <stop offset="0.5" stop-color="var(--photo-blue-mid)"/>
        <stop offset="1" stop-color="var(--photo-blue-dark)"/>
      </radialGradient>
      <linearGradient id="streetTone" x1="0" y1="0" x2="1" y2="1">
        <stop offset="0" stop-color="#e6e6e6"/>
        <stop offset="1" stop-color="#8a8a8a"/>
      </linearGradient>
      <linearGradient id="alleyTone" x1="0" y1="0" x2="1" y2="1">
        <stop offset="0" stop-color="#9a9a9a"/>
        <stop offset="0.5" stop-color="#5c5c5c"/>
        <stop offset="1" stop-color="#2a2a2a"/>
      </linearGradient>
      <linearGradient id="panelTone" x1="0" y1="0" x2="0" y2="1">
        <stop offset="0" stop-color="var(--panel-brown)"/>
        <stop offset="0.55" stop-color="#16130f"/>
        <stop offset="1" stop-color="var(--panel-deep)"/>
      </linearGradient>
      <filter id="softGlow" x="-50%" y="-50%" width="200%" height="200%">
        <feGaussianBlur stdDeviation="10"/>
      </filter>
      <filter id="fineGlow" x="-50%" y="-50%" width="200%" height="200%">
        <feGaussianBlur stdDeviation="2"/>
      </filter>
    </defs>

    <rect class="hero-photo" x="0" y="0" width="916" height="520" fill="url(#heroTone)"
          role="img" aria-label="Photo of a businessman in a suit touching a glowing rising arrow"/>
    <rect class="street-photo" x="938" y="25" width="243" height="181" fill="url(#streetTone)"
          role="img" aria-label="Black and white photo of a New Orleans streetcar on a palm-lined avenue"/>
    <rect class="alley-photo" x="938" y="230" width="243" height="270" fill="url(#alleyTone)"
          role="img" aria-label="Black and white photo of a French Quarter alley beside a cathedral"/>

    <path class="dark-panel" d="M0,160 C300,330 640,515 930,513 C1040,512 1130,480 1200,437 L1200,927 L0,927 Z" fill="url(#panelTone)"/>

    <path class="gold-glow" d="M175,927 C130,820 70,735 0,680" fill="none" stroke="var(--gold-glow)" stroke-width="26" opacity="0.55" filter="url(#softGlow)"/>
    <path class="gold-edge" d="M175,927 C130,820 70,735 0,680" fill="none" stroke="var(--gold)" stroke-width="3" opacity="0.8" filter="url(#fineGlow)"/>
  </svg>

  <p class="intro">If you are receiving this brochure its because someone sees you as a person that doesn’t want to just work and pay bills. Your someone who wants to build real generational wealth. Not throw schemes but the using the greatest wealth builder available. The stock market.</p>

  <h2 class="steps-title">How it works</h2>
  <ol class="steps">
    <li><span class="step-num">1.</span>Make initial deposit. The general partner will invest in stocks, bonds and other investment vehicles on your behalf.</li>
    <li><span class="step-num">2.</span>There is no upfront fees. The general p[partner will guarantee a 5 percent return and will work for free on your behalf until that is achieved. After the 5 percent return on the dollars invested the limited partner will receive 80 percent and the general partner will receive 20 percent of every dollar gained</li>
    <li><span class="step-num">3.</span>As the return and investments multiply the interests begins to compound annually. The legal partner legally owns shares of stock within the club and may redeem once a year or let money continue to earn interest.</li>
  </ol>

  <div class="gains-chart">
    <span class="bar-value fund">28.6 %</span>
    <div class="bar fund"></div>
    <p class="bar-label fund">Harborvale<br>Ventures gains<br>since 2019</p>
    <span class="bar-value index">7.1 %</span>
    <div class="bar index"></div>
    <p class="bar-label index">TR 400<br>gAINS 7.1<br>PERCENT</p>
  </div>
</div>
</body>
</html>
```